Label for Refill packaging eco-conscious beauty brand

We need a label for our refill pouch. Velvet Harbor is an unscented conditioner formulated using the finest healthy & pure ingredients, free of chemicals and harmful toxins. As a minimalist beauty brand we are proud to be certified with TQB, Norvamark and Silver Kestrel.

We already have the pouches and an exciting label for our regular bottles.
We choose a kraft brown packing for the refill pouch and would like something minimalist but elegant for the label.

```html
<!DOCTYPE html>
<html lang="en">
<head>
<meta charset="utf-8">
<title>KLAAR Wende – Velvet Harbor refill label</title>
<link rel="stylesheet" href="https://fonts.googleapis.com/css2?family=Alegreya+Sans:wght@400&family=Montserrat:wght@400;600&display=swap">
<style>
  :root {
    --backdrop: #7b739e;
    --kraft: #c8a985;
    --kraft-light: #cfb28f;
    --ink: #2f312d;
    --mauve: #8a6c84;
  }
  * { margin: 0; padding: 0; box-sizing: border-box; }
  html, body {
    width: 1200px;
    height: 899px;
    overflow: hidden;
    background: var(--backdrop);
  }
  .canvas {
    position: relative;
    width: 1200px;
    height: 899px;
  }
  .label {
    position: absolute;
    left: 304px;
    top: 30px;
    width: 592px;
    height: 840px;
    background: radial-gradient(ellipse at 40% 35%, var(--kraft-light), var(--kraft) 75%);
  }
  .label__frame {
    position: absolute;
    left: 78px;
    top: 76px;
    width: 437px;
    height: 680px;
    border: 2px solid var(--mauve);
    border-radius: 9px;
  }
  .brand {
    position: absolute;
    left: 0;
    width: 100%;
    text-align: center;
    color: var(--ink);
  }
  .brand__mark {
    position: absolute;
    left: 50%;
    top: 188px;
    width: 28px;
    height: 28px;
    margin-left: -14px;
    border-radius: 50%;
    background: var(--ink);
  }
  .brand__name {
    top: 338px;
    font-family: "Alegreya Sans", sans-serif;
    font-weight: 400;
    font-size: 68px;
    line-height: 70px;
    letter-spacing: 1px;
  }
  .product {
    position: absolute;
    left: 0;
    top: 566px;
    width: 100%;
    text-align: center;
  }
  .product__name {
    font-family: "Montserrat", sans-serif;
    font-weight: 600;
    font-size: 38px;
    line-height: 40px;
    color: var(--mauve);
  }
  .product__desc {
    margin-top: 14px;
    font-family: "Montserrat", sans-serif;
    font-weight: 400;
    font-size: 15.5px;
    line-height: 19px;
    color: var(--mauve);
  }
</style>
</head>
<body>
<main class="canvas">
  <section class="label">
    <div class="label__frame"></div>
    <span class="brand__mark" aria-hidden="true"></span>
    <h1 class="brand brand__name">KLAAR<br>Wende</h1>
    <div class="product">
      <h2 class="product__name">Velvet<br>Harbor</h2>
      <p class="product__desc">unscented hair conditioner<br>après-shampoing non parfumé</p>
    </div>
  </section>
</main>
</body>
</html>
```